Business card design needed

New company based in Brisbane, Australia. Brindle Technologies. The business is focused on the delivery of network architecture design and deployment. We will provide both services and the sale of the necessary equipment to deliver the service. Cloud computing is an important element of our focus as this is an emerging market for enterprises in Queensland. Our target marketplace is medium to large corporations with complex infrastructure requirements. IT Management and above will be the typical entry point for us into these accounts. We would like to see the use of various shade of green, design should be clutter free and impress stability, trust and growth.
Updates
Hey Everyone
Just we let you all know we have changed this project to 'committed' payment status.
Looking forward to seeing the designs! Thanks for your efforts.
Best Regards
Martin
Industry/Entity Type
Architecture
Contact Information for Business Card
Brindle Technologies, Martin Coulter, Sales Director, Level 19 Harwell Court, 58 Kelvane Street, Brisbane QLD 4000, Ph +61 7 3946 2271, M +61 4 4208 6157, E martin.coulter@brindletechnologies-example.com.au
Look and feel
Each slider illustrates characteristics of the customer's brand and the style your logo design should communicate.

```html
<!DOCTYPE html>
<html lang="en">
<head>
<meta charset="UTF-8">
<title>Brindle Technologies — Business Card</title>
<link rel="stylesheet" href="https://fonts.googleapis.com/css2?family=Questrial&family=Open+Sans:wght@400;700&display=swap">
<style>
  :root {
    --page-bg: #1c1c1c;
    --card-bg: #050505;
    --brand-green: #5fbf6e;
    --accent-green: #8fd694;
    --text-white: #ffffff;
    --glow-green: rgba(38, 110, 58, 0.55);
    --deep-green: #0e3a1c;
  }
  * { box-sizing: border-box; margin: 0; padding: 0; }
  html, body { width: 1200px; height: 900px; overflow: hidden; background: var(--page-bg); }
  .canvas { position: relative; width: 1200px; height: 900px; }
  .card {
    position: absolute; width: 615px; height: 338px;
    background: var(--card-bg); border-radius: 18px; overflow: hidden;
  }
  .card--front { left: 113px; top: 102px; }
  .card--back { left: 454px; top: 462px; }
  .brand-name {
    position: absolute; font-family: "Questrial", sans-serif; font-weight: 400;
    color: var(--brand-green); font-size: 27px; line-height: 1; letter-spacing: 0.2px; white-space: nowrap;
  }
  .card--front .brand-name { left: 61px; top: 81px; }
  .card--back .brand-name { left: 56px; top: 153px; }
  .brand-dot {
    position: absolute; width: 11px; height: 11px; border-radius: 50%;
    background: var(--brand-green);
  }
  .card--front .brand-dot { left: 40px; top: 90px; }
  .card--back .brand-dot { left: 35px; top: 162px; }
  .holder {
    position: absolute; left: 60px; top: 165px; font-family: "Open Sans", sans-serif;
    display: inline-flex; flex-direction: column; align-items: flex-end;
  }
  .holder-name { color: var(--text-white); font-weight: 700; font-size: 22px; line-height: 1.1; }
  .holder-role { color: var(--brand-green); font-weight: 700; font-size: 13px; line-height: 1.2; }
  .contacts { position: absolute; left: 59px; top: 249px; list-style: none; font-family: "Open Sans", sans-serif; }
  .contacts li {
    display: flex; align-items: center; gap: 5px; height: 17px;
    color: var(--accent-green); font-size: 12px; white-space: nowrap;
  }
  .contacts svg { width: 10px; height: 10px; fill: var(--text-white); flex: none; }
  .wave-field { position: absolute; }
  .card--front .wave-field {
    left: 370px; top: 0; width: 245px; height: 250px;
    background: radial-gradient(ellipse at 70% 40%, var(--deep-green) 0%, rgba(14,58,28,0.4) 45%, transparent 72%);
  }
  .card--back .wave-field--upper {
    left: 360px; top: 0; width: 255px; height: 300px;
    background: radial-gradient(ellipse at 65% 45%, var(--deep-green) 0%, rgba(14,58,28,0.45) 45%, transparent 72%);
  }
  .card--back .wave-field--lower {
    left: 0; top: 255px; width: 480px; height: 83px;
    background: radial-gradient(ellipse at 35% 70%, var(--glow-green) 0%, rgba(14,58,28,0.3) 45%, transparent 75%);
  }
</style>
</head>
<body>
<main class="canvas">
  <section class="card card--front" aria-label="Business card front">
    <div class="wave-field" role="img" aria-label="Decorative flowing lines ending in dots"></div>
    <span class="brand-dot"></span>
    <h1 class="brand-name">Brindle Technologies</h1>
    <div class="holder">
      <p class="holder-name">Martin Coulter</p>
      <p class="holder-role">Sales Director</p>
    </div>
    <ul class="contacts">
      <li><svg viewBox="0 0 10 10"><path d="M2.5 0h5a1 1 0 0 1 1 1v8a1 1 0 0 1-1 1h-5a1 1 0 0 1-1-1V1a1 1 0 0 1 1-1zm0 1.5v6h5v-6z"/></svg>+61 4 4208 6157</li>
      <li><svg viewBox="0 0 10 10"><path d="M2 0.5l1.8 2-1 1.2c.6 1.3 1.5 2.2 2.7 2.8l1.2-1 2 1.8-1 1.6C4.5 8.8 1.2 5.5.4 2z"/></svg>+61 7 3946 2271</li>
      <li><svg viewBox="0 0 10 10"><path d="M5 0a3.3 3.3 0 0 1 3.3 3.3C8.3 6 5 10 5 10S1.7 6 1.7 3.3A3.3 3.3 0 0 1 5 0zm0 2a1.3 1.3 0 1 0 0 2.6A1.3 1.3 0 0 0 5 2z"/></svg>Level 19 Harwell Court, 58 Kelvane Street, Brisbane QLD 4000</li>
      <li><svg viewBox="0 0 10 10"><path d="M0 2h10v6H0zm1 .8L5 5.5 9 2.8z"/></svg>martin.coulter@brindletechnologies-example.com.au</li>
    </ul>
  </section>

  <section class="card card--back" aria-label="Business card back">
    <div class="wave-field wave-field--upper" role="img" aria-label="Decorative flowing lines ending in dots"></div>
    <div class="wave-field wave-field--lower" role="img" aria-label="Decorative flowing line band"></div>
    <span class="brand-dot"></span>
    <h2 class="brand-name">Brindle Technologies</h2>
  </section>
</main>
</body>
</html>
```